Vascular Secialist needs a tri-fold brochure

I would like to create a tri- fold of all the services that the vascular practice offers. The practice specializes in lower extremity vascular diseases. I would like to have the tri-fold have brief descriptions of all the services as well as images of the practice to show case the top of the line technology. The trip-fold will be front in back with a crisp modern design. The diseases that they treat are: arterial disease, venous disease, varicose veins, chronic venous insufficiency, deep vein thrombosis, uterine fibroids, pelvic and labial varicose veins, varicocele. Treatment options for all diseases that the practice treats.

Target Market(s)

Doctors

Industry/Entity Type

Medical

Font styles to use
Other font styles liked:
• Myriod Pro SemiExtende

Colors
33a6d7
86cae7
aaaaaa
85cae6
dcedf6
cee9f5
757575
9d9d9d
c3c3c3

Requirements
Must have
• creativity and taglines that capture the reader
Nice to have
• I would like the piece to mirror the website. www.larvinmesaclinic.com

```html
<!DOCTYPE html>
<html lang="en">
<head>
<meta charset="utf-8">
<title>Larvin Mesa Clinic – Tri-fold Brochure</title>
<link href="https://fonts.googleapis.com/css2?family=Oswald:wght@300;400&family=Source+Sans+3:wght@400;600&display=swap" rel="stylesheet">
<style>
  :root {
    --page-bg: #e4e4e4;
    --paper: #ffffff;
    --paper-grey: #f3f3f3;
    --panel-blue: #6fa9d3;
    --band-blue: #86b9dc;
    --accent: #3d8fc5;
    --bright: #33a6d7;
    --dark: #444444;
    --mid: #757575;
    --text: #333333;
    --photo-light: #cfd8dd;
  }
  * { box-sizing: border-box; margin: 0; padding: 0; }
  html, body { width: 1200px; height: 1200px; overflow: hidden; background: var(--page-bg); }
  body { font-family: "Source Sans 3", sans-serif; color: var(--text); position: relative; }

  .sheet { position: absolute; left: 203px; width: 794px; height: 560px; background: var(--paper); box-shadow: 0 2px 8px rgba(0,0,0,.18); overflow: hidden; }
  .sheet--outside { top: 25px; }
  .sheet--inside { top: 615px; }
  .sheet-art { position: absolute; inset: 0; width: 794px; height: 560px; }

  .panel { position: absolute; top: 0; width: 265px; height: 560px; }
  .panel--1 { left: 0; } .panel--2 { left: 265px; } .panel--3 { left: 529px; }

  .copy { position: absolute; left: 30px; width: 206px; font-size: 7px; line-height: 1.62; text-align: justify; hyphens: auto; }
  .copy p { margin-bottom: 5px; }
  .copy h3 { font-weight: 400; font-size: 7.6px; color: var(--accent); margin: 6px 0 3px; }
  .copy h3.plain { color: var(--text); }
  .copy h4 { font-weight: 600; font-size: 8.4px; color: var(--text); margin: 6px 0 4px; }
  .copy--onblue { color: #ffffff; }
  .copy--onblue h3 { color: #ffffff; font-weight: 600; }

  .headline { position: absolute; left: 0; width: 265px; text-align: center; font-family: "Oswald", sans-serif; font-weight: 400; line-height: 1.15; color: #222; }
  .headline .hl { color: var(--bright); font-weight: 300; }
  .headline--top { top: 35px; font-size: 16px; }
  .headline--tag { top: 452px; font-size: 17px; }

  .contact { position: absolute; top: 382px; left: 0; width: 265px; text-align: center; color: #fff; font-size: 11.5px; line-height: 1.35; }
  .contact dt { margin-top: 14px; }
  .contact dt:first-child { margin-top: 0; }

  .brand { position: absolute; top: 52px; left: 0; width: 265px; display: flex; align-items: center; justify-content: center; gap: 10px; }
  .brand-mark { width: 22px; height: 22px; border-radius: 50%; background: var(--dark); }
  .brand-name { font-family: "Source Sans 3", sans-serif; font-weight: 400; font-size: 22px; color: var(--dark); letter-spacing: 1px; line-height: 1; }

  .website { position: absolute; top: 526px; left: 0; width: 265px; text-align: center; font-size: 8.5px; letter-spacing: 1.6px; color: #222; }
</style>
</head>
<body>

<!-- Outside of the brochure -->
<section class="sheet sheet--outside">
  <svg class="sheet-art" viewBox="0 0 794 560" aria-hidden="false">
    <!-- panel 1 -->
    <rect x="0" y="0" width="265" height="300" fill="#f6f6f6"/>
    <polygon points="0,270 265,312 265,328 0,286" fill="var(--dark)"/>
    <polygon points="0,286 265,328 265,336 0,292" fill="#bdbdbd"/>
    <rect x="0" y="542" width="265" height="18" fill="var(--band-blue)"/>
    <!-- panel 2 -->
    <rect x="265" y="0" width="265" height="560" fill="var(--paper-grey)"/>
    <polygon points="265,188 530,94 530,104 265,198" fill="var(--band-blue)"/>
    <polygon points="265,198 530,104 530,378 265,338" fill="var(--photo-light)" role="img" aria-label="Photo of the clinic's bright waiting lounge with tall windows and benches"/>
    <polygon points="265,338 530,378 530,386 265,350" fill="#d9d9d9"/>
    <polygon points="265,350 530,386 530,542 265,542" fill="var(--panel-blue)"/>
    <rect x="265" y="542" width="265" height="18" fill="var(--dark)"/>
    <!-- panel 3 -->
    <rect x="529" y="0" width="265" height="560" fill="var(--paper-grey)"/>
    <rect x="559" y="126" width="210" height="304" fill="#5a3a2a"/>
    <rect x="562" y="129" width="204" height="298" fill="#8d9aa4" role="img" aria-label="Portrait of the lead vascular surgeon in blue scrubs, arms crossed"/>
    <polygon points="529,445 794,430 794,460 529,470" fill="var(--paper-grey)"/>
    <polygon points="529,412 794,470 794,560 529,560" fill="#ffffff"/>
    <rect x="529" y="542" width="265" height="18" fill="var(--band-blue)"/>
  </svg>

  <div class="panel panel--1">
    <div class="copy" style="top:26px">
      <p>Our conveniently located, state-of-art facility is designed for your patients comfort and utilizes cutting edge technology to provide minimally invasive treatments. Personable staff members make every visit a positive experience, with short wait times and an efficient, stream-lined process that ensures your patients leave feeling educated and confident that they are in good hands for all their vascular needs.</p>
      <h4>Diseases we treat:</h4>
      <h3>Peripheral Arterial Disease</h3>
      <p>Peripheral Arterial Disease (PAD) develops when the arteries in the legs build up plaque, obstructing and narrowing the arteries and preventing blood, oxygen, glucose from flowing properly to tissue. This lack of blood-flow causes pain, cramping, and swelling in the legs as the muscles and tissue starve for blood and if untreated, can lead to amputation of the toes and/or foot.</p>
    </div>
    <div class="copy" style="top:324px">
      <h3>Varicose Veins</h3>
      <p>Closely related to chronic venous insufficiency, varicose veins are enlarged veins that are visible through the skin. The veins often appear bulging or twisted and are generally larger than three millimeters in diameter. Varicose veins affect one out of two people over the age of 50, and women who have had children are particularly susceptible.</p>
      <h3 class="plain">Deep Venous Thrombosis</h3>
      <p style="margin-top:-3px">A DVT is the formation of a blood clot (thrombus) in a deep veins, most commonly occurring in the legs. This thrombus disrupts the normal flow of blood from the legs or arms back to the heart. A DVT presents a serious risk to your life; the clot could move to your heart or lungs causing serious and sometimes fatal conditions. You must see a doctor immediately if you think you may have a DVT.</p>
    </div>
  </div>

  <div class="panel panel--2">
    <h1 class="headline headline--top">The Leading Vascular Surgery<br><span class="hl">Facility for Treating Arterial</span><br>Disease and Venous Disease.</h1>
    <dl class="contact">
      <dt>Call:</dt><dd>(555) 310-4826</dd>
      <dt>Fax</dt><dd>(555) 310-4827</dd>
      <dt>Address</dt><dd>1280 Larvin Mesa Drive<br>Cedar Vale, CA 90000</dd>
    </dl>
  </div>

  <div class="panel panel--3">
    <div class="brand"><span class="brand-mark"></span><span class="brand-name">LARVIN MESA</span></div>
    <h2 class="headline headline--tag">Leading vascular facility<br><span class="hl">specializing in treatment</span><br>of lower extremity arterial<br><span class="hl">and venous disease</span></h2>
  </div>
</section>

<!-- Inside of the brochure -->
<section class="sheet sheet--inside">
  <svg class="sheet-art" viewBox="0 0 794 560">
    <!-- panel 1 -->
    <polygon points="0,488 265,530 265,560 0,560" fill="var(--band-blue)"/>
    <polygon points="0,488 265,530 265,520 0,478" fill="var(--dark)"/>
    <rect x="82" y="472" width="100" height="62" fill="#b9c3ca" role="img" aria-label="Laptop showing two doctors, with a stethoscope beside it"/>
    <!-- panel 2 -->
    <rect x="265" y="0" width="265" height="110" fill="#e3ebf1" role="img" aria-label="Photo of a doctor holding a stethoscope toward the viewer"/>
    <polygon points="265,64 530,110 530,118 265,74" fill="var(--dark)"/>
    <polygon points="265,74 530,118 530,460 265,503" fill="var(--panel-blue)"/>
    <!-- panel 3 -->
    <rect x="529" y="0" width="265" height="150" fill="#dfe3e6" role="img" aria-label="Group photo of the clinic's medical team in white coats"/>
    <polygon points="529,140 794,108 794,122 529,154" fill="var(--dark)"/>
    <polygon points="529,154 794,122 794,160 529,160" fill="#ffffff"/>
    <polygon points="529,458 794,438 794,560 529,560" fill="#e8ddd5" role="img" aria-label="Close-up photo of a patient's hands resting on a bed"/>
  </svg>

  <div class="panel panel--1">
    <div class="copy" style="top:14px">
      <h3 class="plain" style="margin:0">Varicocele</h3>
      <h3 style="margin:0 0 3px">A male condition</h3>
      <p>A varicocele (VAR-ih-koe-seel) is an enlargement of the veins within the scrotum. A varicocele is similar to a varicose vein that can occur in the legs or in the female pelvic area. 15% of the general male population suffer from varicocele with more than 80% occurring on the left side and the remainder on both sides. They are generally acquired during puberty. Most varicoceles are asymptomatic; however, some can cause scrotal pain. This pain is generally mild to moderate, occurs with long periods of sitting, standing or activity and is relieved by lying down. Although it can be uncomfortable before bedtime, it generally does not occur upon awakening after a night's rest. The pain is dull, "tooth ache" like and generally doesn't refer elsewhere. The resulting backup causes the veins to widen (dilate) which can lead to damage to the testicle and result in worsened fertility. Our physicians can provide targeted treatment for varicocele called "varicocele repair."</p>
      <h3>Pelvic Venous Congestion (PVCS)</h3>
      <p>Pelvic venous congestion syndrome (PVCS) also known as ovarian vein reflux, causes chronic pelvic pain in approximately 13-40% of women. The ovarian veins carry venous blood from the ovaries and pelvis up to the level of the renal veins in the abdomen. All veins have valves to help guide blood flow back up towards the heart. When these valves become damaged or dysfunctional, some blood flows backwards causing the veins to become engorged or 'congested,' leading to varicose veins. PVCS is essentially varicose veins in the pelvis due to venous insufficiency in the ovarian veins. These internal varicose veins can cause chronic, debilitating pain.</p>
    </div>
  </div>

  <div class="panel panel--2">
    <div class="copy copy--onblue" style="top:116px">
      <h3>Pelvic and Labial Varicose Veins</h3>
      <p>Pelvic varicose veins and labial varicose veins are forms of venous insufficiency by which women's pelvic, labial, or vulvar veins become enlarged and dilated during pregnancy and continue after the baby has been delivered. Such varicosities often worsen with each pregnancy. Some women develop frequent or continuous pain from labial varicosities prominent during pregnancy and improve after the baby is born. Labial varicose veins may be due to iliac vein obstruction from compression or old clots, or they may be due to ovarian vein reflux with pelvic venous insufficiency. In some patients, the primary problem is reflux in the veins of the deep pelvis. Like with all types of venous reflux disease, our physicians provide targeted treatments that divert blood flow through healthy veins and eliminate discomfort.</p>
      <h3>Uterine Fibroids</h3>
      <p>Uterine fibroids (fibroid tumors, leiomyomas, or myomas) are benign masses that grow on the outside or in the muscle wall of the uterus. Fibroids are very common in women in their 30s and 40s— as many 70%-80% of all women will have fibroids by age 50. While the cause of Fibroids is not conclusively proven, they seem to be linked with the female hormones estrogen and progesterone. Fibroids can range in number and size from a single growth to multiple growths, and from very small to very large.</p>
    </div>
    <p class="website">www.larvinmesaclinic.com</p>
  </div>

  <div class="panel panel--3">
    <div class="copy" style="top:166px">
      <h3 style="margin-top:0">Patient Story</h3>
      <p>Female, age 91 referred by her podiatrist for gangrene, non-healing wounds on her toes, and absent pulse in the foot. This patient was referred by her podiatrist for an emergency evaluation of her left foot. The foot was progressively darkening (turning black due to lack of blood flow), had no detectable pulse, and had two non-healing wounds on the toes. Due to her absent arterial flow through the leg, the foot was no longer receiving any oxygen and was quickly dying; she was at a critical risk for amputation. Following her ultrasound, she was immediately scheduled for intervention. Dr. Harlan treated her arteries with thorough athrectomy, stenting, and angioplasty all the way down into her foot to create a clear arterial blood flow through the limb. With restored blood flow, the color in her foot slowly returned to normal, her pulse returned, and her wounds began to heal.</p>
      <p>Before treatment (image 1) she had no arteries flowing down into the foot causing the slow death of the foot. After extensive treatment (image 2), she had two strong arteries flowing into the foot and she began to recover.</p>
    </div>
  </div>
</section>

</body>
</html>
```